GPS Tracker Business Card Design

We need a business card for a GPS Vehicle tracking company. We sell the hardware for the vehicle and the software platform to monitor your vehicle/s. Including high asset non-powered vehicles like a trailer using our solar powered unit.
We like using dark blue to different shades of blue along with gold. We have phone apps for Android and Apple devices.

We have a platform for families wanting to track their teenage driver and children; Plus a Fleet vehicle tracking platform.

Features: unlimited number of vehicles and/or assets including snow mobiles forklifts generators trailers airport equipment

Reports for driving behavior reports and alerts dashboard fleet maintenace timeline view and replay geofence real time alerts logbook scheduling route optimization accounting integration fleet grouping closest vehicle locator On Board Diagnostics.

Benefits: Increased productivity improved fuel efficiency organizing your business improve time management simplify back end processes, reduce fleet fuel efficiency and expenses increase fleet security etc..

Please view website: Velmora.com

Industry/Entity Type

Business

Contact Information for Business Card

Harold B Pennick

```html
<!DOCTYPE html>
<html lang="en">
<head>
<meta charset="utf-8">
<title>Velmora Business Card</title>
<link rel="stylesheet" href="https://fonts.googleapis.com/css2?family=Open+Sans:wght@300;400;600&display=swap">
<style>
  :root {
    --backdrop: #e9e6e2;
    --card-white: #ffffff;
    --brand-blue: #1352a0;
    --name-blue: #1a5aa8;
    --ink-dark: #1e2a3a;
    --text-grey: #6b6b6b;
    --tagline-grey: #7a7a7a;
    --icon-blue: #1a5aa8;
  }
  * { margin: 0; padding: 0; box-sizing: border-box; }
  html, body {
    width: 1200px; height: 1000px; overflow: hidden;
    background: var(--backdrop);
    font-family: "Open Sans", Arial, sans-serif;
  }
  .canvas { position: relative; width: 1200px; height: 1000px; }
  .card {
    position: absolute; left: 265px; width: 666px; height: 398px;
    border-radius: 28px;
    box-shadow: 0 4px 12px rgba(0,0,0,0.18);
  }
  .card-front { top: 73px; background: var(--card-white); }
  .card-back { top: 532px; background: var(--brand-blue); }

  .brand { position: absolute; text-align: left; }
  .brand-name { font-weight: 300; letter-spacing: -1px; line-height: 1; }
  .brand-tagline { font-weight: 400; line-height: 1; }

  .card-front .brand { left: 33px; top: 152px; }
  .card-front .brand-name { font-size: 58px; color: var(--ink-dark); }
  .card-front .brand-tagline { font-size: 19px; color: var(--tagline-grey); margin-top: 8px; margin-left: 16px; }

  .card-back .brand { left: 0; width: 666px; top: 143px; text-align: center; }
  .card-back .brand-name { font-size: 66px; color: #ffffff; }
  .card-back .brand-tagline { font-size: 22px; color: #ffffff; margin-top: 14px; }

  .contact-block { position: absolute; left: 382px; top: 78px; color: var(--text-grey); font-size: 16px; }
  .person-name { font-size: 22px; font-weight: 600; color: var(--name-blue); line-height: 28px; }
  .person-title { line-height: 22px; }
  .address { margin-top: 28px; line-height: 23px; }
  .contact-list { list-style: none; margin-top: 20px; }
  .contact-list li { display: flex; align-items: center; height: 23.5px; }
  .contact-list svg { width: 15px; height: 15px; margin-right: 8px; fill: var(--icon-blue); }
</style>
</head>
<body>
<div class="canvas">
  <section class="card card-front">
    <div class="brand">
      <div class="brand-name">Velmora</div>
      <div class="brand-tagline">Every Route, Every Mile</div>
    </div>
    <div class="contact-block">
      <div class="person-name">Harold B Pennick</div>
      <div class="person-title">Managing Parthner</div>
      <div class="address">27 Corella Ridge Rd<br>Wattlebank, QLD, 4215</div>
      <ul class="contact-list">
        <li><svg viewBox="0 0 16 16" aria-hidden="true"><path d="M1 5c0-2 3-3 7-3s7 1 7 3v1h-3V5H4v1H1z"/><rect x="3" y="7" width="10" height="7" rx="1"/></svg>+ 000 000 0000</li>
        <li><svg viewBox="0 0 16 16" aria-hidden="true"><rect x="4" y="1" width="8" height="4"/><rect x="1" y="6" width="14" height="6" rx="1"/><rect x="4" y="10" width="8" height="5" fill="#fff" stroke="#1a5aa8" stroke-width="1.5"/></svg>+ 000 000 0000</li>
        <li><svg viewBox="0 0 16 16" aria-hidden="true"><rect x="1" y="3" width="14" height="10"/><path d="M1.5 3.5 8 9l6.5-5.5" fill="none" stroke="#fff" stroke-width="1.3"/></svg>info@Velmora.com</li>
        <li><svg viewBox="0 0 16 16" aria-hidden="true"><circle cx="7" cy="7" r="6"/><path d="M3 5h8M3 9h8M7 1c-2 3-2 9 0 12M7 1c2 3 2 9 0 12" fill="none" stroke="#fff" stroke-width="1"/><path d="M9 9l6 3-2.5 1L11 15.5z"/></svg>www.Velmora.com</li>
      </ul>
    </div>
  </section>
  <section class="card card-back">
    <div class="brand">
      <div class="brand-name">Velmora</div>
      <div class="brand-tagline">Every Route, Every Mile</div>
    </div>
  </section>
</div>
</body>
</html>
```